Information One Page for Email

I am looking for a informative attachment I can send with an introductive email for Maplecrest Slab Works. Something I can also Mail.

Maplecrest Slab Works is the leader in Rebar Post Tension Cable Placement and Post Tension Cable repair. Outside of cable placement and repair we do concrete repair, Parking Garage restoration and

Content

Post Tension Repair and Concrete Restoration
Post-tensioning is a revolutionary method in concrete construction that enhances the strength and durability of structures. However, like all construction ele-ments, post-tension cables can experience wear and damage over time. Ensuring timely and effective repair is crucial for maintaining the safety and integrity of your building.
Why Post-Tension Cable Repair is Essential
1. **Structural Integrity**: Damaged or deteriorated cables can compromise the structural integrity of your building, leading to safety hazards and potential structural failures.
2. **Extended Lifespan**: Regular maintenance and repair of post-tension cables extend the lifespan of your structure, ensuring it remains safe and function-al for years to come.
3. **Cost-Effective**: Addressing cable issues early on prevents more severe damage and costly repairs down the line.
Common Signs of Post-Tension Cable Issues
- Cracks in concrete surfaces
- Unusual noises or popping sounds
- Visible cable ends or broken strands
- Water leakage through cracks
Our Repair Process
1. **Inspection and Assessment**: Our team conducts a thorough inspection to identify the extent of the damage and determine the appropriate repair meth-ods.
2. **Cable Repair or Replacement**: Depending on the severity, we either re-pair the existing cables or replace them with new ones to restore full functional-ity.
3. **Sealing and Protection**: After repairing, we seal the affected areas to protect against moisture and future damage.
4. **Quality Assurance**: We perform rigorous quality checks to ensure the repairs meet industry standards and the structure is safe for use.
Why Choose Us
- **Expertise and Experience**: With years of experience in post-tension cable repair, our team is skilled in handling even the most complex repairs efficiently and effectively.
- **Advanced Technology**: We use the latest technology and materials to ensure durable and long-lasting repairs.
- **Customer Satisfaction**: Our commitment to quality and customer satisfaction sets us apart. We work closely with our clients to ensure their needs are met and expectations exceeded.
Contact Us
If you suspect issues with your post-tension cables or need a routine inspection, don't hesitate to contact us. Our experts are ready to provide the best solutions to keep your structures safe and secure.
Ensure the safety and longevity of your building with our professional post-tension cable repair services. Trust us to deliver quality and reliability every time.

```html
<!DOCTYPE html>
<html lang="en">
<head>
<meta charset="utf-8">
<title>Maplecrest Slab Works – Post Tension Repair</title>
<link rel="stylesheet" href="https://fonts.googleapis.com/css2?family=Saira+Semi+Condensed:wght@400;500;600;700&display=swap">
<style>
:root{
  --green:#0a6a36;
  --green-dark:#05492a;
  --green-light:#4fae3e;
  --lime:#2ccf3c;
  --charcoal:#2a2a2a;
  --charcoal-head:#3b3b3b;
  --grey-chev:#454545;
  --gold:#c7b31e;
  --ink:#141414;
  --sky-top:#bcdcf5;
  --sky-bottom:#e6f1fb;
  --backdrop:#b9b9b9;
}
*{margin:0;padding:0;box-sizing:border-box}
html,body{width:993px;height:1200px;overflow:hidden;background:var(--backdrop);font-family:"Saira Semi Condensed",sans-serif}
.flyer{position:absolute;left:81px;top:85px;width:803px;height:1039px;background:#fff;overflow:hidden;box-shadow:0 2px 8px rgba(0,0,0,.25)}
.sky{position:absolute;left:0;top:0;width:803px;height:356px;background:linear-gradient(180deg,var(--sky-top),var(--sky-bottom))}
.band{position:absolute;left:0;top:356px;width:803px;height:60px;background:linear-gradient(180deg,#fff,var(--sky-bottom))}
.photo{position:absolute;left:0;top:0}
.brand-plate{position:absolute;left:0;top:0}
.brand-name{position:absolute;left:34px;top:38px;width:200px;font-size:22px;font-weight:700;line-height:1.1;color:var(--green)}
.headline{position:absolute;left:36px;top:124px;font-size:35px;font-weight:700;line-height:37px;color:var(--ink)}
.headline span{color:var(--green);display:block}
.intro{position:absolute;left:37px;top:216px;width:450px;font-size:11px;line-height:14.3px;color:var(--ink)}
.panel{position:absolute;top:301px;width:358px;height:375px;color:#fff}
.panel svg{position:absolute;left:0;top:0}
.panel-green{left:34px}
.panel-dark{left:410px}
.panel h2{position:absolute;left:33px;font-size:23px;font-weight:700;line-height:31px}
.panel-green h2{top:11px}
.panel-dark h2{top:27px}
.point{position:absolute;left:34px;width:300px}
.point h3{font-size:18px;font-weight:700;line-height:22px;padding-left:33px;position:relative}
.point h3 svg{position:absolute;left:0;top:2px}
.point p{font-size:12.6px;line-height:16px;margin-top:4px}
.process-title{position:absolute;left:0;top:688px;width:803px;text-align:center;font-size:21px;font-weight:700;color:var(--grey-chev)}
.process-title span{color:var(--green)}
.chevrons{position:absolute;left:0;top:722px}
.step{position:absolute;top:722px;width:170px;height:137px;text-align:center;color:#fff}
.step svg{display:block;margin:8px auto 0}
.step h4{font-size:11.5px;font-weight:700;margin-top:4px}
.step p{font-size:8.6px;line-height:12px;margin-top:2px;padding:0 8px}
.signs-title{position:absolute;left:39px;top:876px;font-size:17px;font-weight:700;line-height:22px;color:var(--green)}
.sign{position:absolute;top:880px;font-size:11.5px;font-weight:500;line-height:15px;color:var(--ink);padding-left:32px}
.sign svg{position:absolute;left:0;top:0}
.signs-line{position:absolute;left:0;top:0}
.closing{position:absolute;top:955px;width:360px;font-size:11.4px;font-weight:700;line-height:14.4px;color:var(--ink)}
.footer-bar{position:absolute;left:0;top:1027px}
</style>
</head>
<body>
<main class="flyer">
  <div class="sky"></div>
  <div class="band"></div>

  <svg class="photo" width="803" height="356" role="img" aria-label="Photo of a concrete building under repair with exposed slab edges and shoring, seen from below">
    <defs><linearGradient id="photoTone" x1="0" y1="0" x2="1" y2="1">
      <stop offset="0" stop-color="#d9d6cf"/><stop offset=".6" stop-color="#a9a49a"/><stop offset="1" stop-color="#5b5850"/>
    </linearGradient></defs>
    <polygon points="582,0 803,0 803,356 479,356" fill="url(#photoTone)"/>
  </svg>

  <svg class="brand-plate" width="300" height="125">
    <polygon points="0,0 279,0 242,115 0,108" fill="#fff"/>
    <polygon points="279,0 242,115 0,108 0,106 232,108" fill="var(--lime)"/>
  </svg>
  <div class="brand-name">Maplecrest Slab Works</div>

  <h1 class="headline">Post Tension Repair and<span>Concrete Restoration</span></h1>
  <p class="intro">Post-tensioning is a revolutionary method in concrete construction that enhances the strength and durability of structures. However, like all construction ele-ments, post-tension cables can experience wear and damage over time. Ensuring timely and effective repair is crucial for maintaining the safety and integrity of your building.</p>

  <section class="panel panel-green">
    <svg width="358" height="375">
      <defs><linearGradient id="greenHead" x1="0" x2="1"><stop offset="0" stop-color="#053c22"/><stop offset="1" stop-color="var(--green)"/></linearGradient></defs>
      <rect y="83" width="358" height="292" fill="var(--green)"/>
      <polygon points="0,0 307,0 358,54 358,83 0,83" fill="url(#greenHead)"/>
    </svg>
    <h2>Why Post-Tension<br>Cable Repair is Essential</h2>
    <div class="point" style="top:100px"><h3><svg width="25" height="18"><rect x="1" y="2" width="15" height="14" fill="none" stroke="var(--gold)" stroke-width="2.4"/><path d="M5 8l4 4 14-11" fill="none" stroke="var(--gold)" stroke-width="2.6"/></svg>Structural Integrity</h3><p>Damaged or deteriorated cables can compromise the structural integrity of your building, leading to safety hazards and potential structural failures.</p></div>
    <div class="point" style="top:191px"><h3><svg width="25" height="18"><rect x="1" y="2" width="15" height="14" fill="none" stroke="var(--gold)" stroke-width="2.4"/><path d="M5 8l4 4 14-11" fill="none" stroke="var(--gold)" stroke-width="2.6"/></svg>Extended Lifespan</h3><p>Regular maintenance and repair of post-tension cables extend the lifespan of your structure, ensuring it remains safe and function-al for years to come.</p></div>
    <div class="point" style="top:282px"><h3><svg width="25" height="18"><rect x="1" y="2" width="15" height="14" fill="none" stroke="var(--gold)" stroke-width="2.4"/><path d="M5 8l4 4 14-11" fill="none" stroke="var(--gold)" stroke-width="2.6"/></svg>Cost-Effective</h3><p>Addressing cable issues early on prevents more severe damage and costly repairs down the line.</p></div>
  </section>

  <section class="panel panel-dark">
    <svg width="358" height="375">
      <defs><linearGradient id="darkHead" x1="0" x2="1"><stop offset="0" stop-color="#323232"/><stop offset="1" stop-color="#4a4a4a"/></linearGradient></defs>
      <rect y="83" width="358" height="292" fill="var(--charcoal)"/>
      <polygon points="0,0 307,0 358,54 358,83 0,83" fill="url(#darkHead)"/>
    </svg>
    <h2>Why Choose Us</h2>
    <div class="point" style="top:100px"><h3><svg width="25" height="18"><rect x="1" y="2" width="15" height="14" fill="none" stroke="var(--gold)" stroke-width="2.4"/><path d="M5 8l4 4 14-11" fill="none" stroke="var(--gold)" stroke-width="2.6"/></svg>Expertise and Experience</h3><p>With years of experience in post-tension cable repair, our team is skilled in handling even the most complex repairs efficiently and effectively.</p></div>
    <div class="point" style="top:191px"><h3><svg width="25" height="18"><rect x="1" y="2" width="15" height="14" fill="none" stroke="var(--gold)" stroke-width="2.4"/><path d="M5 8l4 4 14-11" fill="none" stroke="var(--gold)" stroke-width="2.6"/></svg>Advanced Technology</h3><p>We use the latest technology and materials to ensure durable and long-lasting repairs.</p></div>
    <div class="point" style="top:275px"><h3><svg width="25" height="18"><rect x="1" y="2" width="15" height="14" fill="none" stroke="var(--gold)" stroke-width="2.4"/><path d="M5 8l4 4 14-11" fill="none" stroke="var(--gold)" stroke-width="2.6"/></svg>Customer Satisfaction</h3><p>Our commitment to quality and customer satisfaction sets us apart. We work closely with our clients to ensure their needs are met and expectations exceeded.</p></div>
  </section>

  <h2 class="process-title"><span>OUR</span> REPAIR PROCESS</h2>
  <svg class="chevrons" width="803" height="137">
    <defs><linearGradient id="chevGreen" x1="0" y1="1" x2="1" y2="0"><stop offset="0" stop-color="var(--green)"/><stop offset="1" stop-color="#7cc443"/></linearGradient></defs>
    <polygon points="36,0 201,0 233,68 201,137 36,137 68,68" fill="url(#chevGreen)"/>
    <polygon points="214,0 379,0 411,68 379,137 214,137 246,68" fill="var(--grey-chev)"/>
    <polygon points="392,0 557,0 589,68 557,137 392,137 424,68" fill="url(#chevGreen)"/>
    <polygon points="570,0 735,0 767,68 735,137 570,137 602,68" fill="var(--grey-chev)"/>
  </svg>
  <div class="step" style="left:57px"><svg width="40" height="40" fill="none" stroke="#fff" stroke-width="2"><circle cx="22" cy="17" r="11"/><path d="M14 25L4 36"/><path d="M16 19l4-4 3 3 5-6"/></svg><h4>Inspection and Assessment</h4><p>Our team conducts a thorough inspection to identify the extent of the damage and determine the appropriate repair meth-ods.</p></div>
  <div class="step" style="left:235px"><svg width="40" height="40" fill="none" stroke="#fff" stroke-width="2.2"><path d="M34 6H12a7 7 0 0 0 0 14h16a7 7 0 0 1 0 14H6"/><path d="M18 15l3 3M22 13v3M24 17h3"/></svg><h4>Cable Repair or Replacement</h4><p>Depending on the severity, we either re-pair the existing cables or replace them with new ones to restore full functional-ity.</p></div>
  <div class="step" style="left:413px"><svg width="40" height="40" fill="none" stroke="#fff" stroke-width="2"><path d="M20 3l10 4v8c0 7-5 11-10 13-5-2-10-6-10-13V7z"/><path d="M15 15l4 4 6-7"/><path d="M3 24l6 8h5M37 24l-6 8h-5"/></svg><h4>Sealing and Protection</h4><p>After repairing, we seal the affected areas to protect against moisture and future damage.</p></div>
  <div class="step" style="left:591px"><svg width="40" height="40" fill="none" stroke="#fff" stroke-width="2"><path d="M18 4l13 5v10c0 9-6 14-13 17C11 33 5 28 5 19V9z"/><circle cx="18" cy="19" r="5"/><circle cx="32" cy="9" r="6"/><path d="M29 9l2 2 4-4"/></svg><h4>Quality Assurance</h4><p>We perform rigorous quality checks to ensure the repairs meet industry standards and the structure is safe for use.</p></div>

  <h3 class="signs-title">Common Signs of<br>Post-Tension Cable Issues</h3>
  <div class="sign" style="left:247px"><svg width="26" height="26" fill="none" stroke="var(--green-light)" stroke-width="2.2"><rect x="6" y="6" width="14" height="14" transform="rotate(45 13 13)"/><path d="M8 13l4 4 6-7"/></svg>Cracks in concrete<br>surfaces</div>
  <div class="sign" style="left:378px"><svg width="26" height="26" fill="none" stroke="var(--green-light)" stroke-width="2.2"><rect x="6" y="6" width="14" height="14" transform="rotate(45 13 13)"/><path d="M8 13l4 4 6-7"/></svg>Unusual noises<br>or popping sounds</div>
  <div class="sign" style="left:510px"><svg width="26" height="26" fill="none" stroke="var(--green-light)" stroke-width="2.2"><rect x="6" y="6" width="14" height="14" transform="rotate(45 13 13)"/><path d="M8 13l4 4 6-7"/></svg>Visible cable ends<br>or broken strands</div>
  <div class="sign" style="left:641px"><svg width="26" height="26" fill="none" stroke="var(--green-light)" stroke-width="2.2"><rect x="6" y="6" width="14" height="14" transform="rotate(45 13 13)"/><path d="M8 13l4 4 6-7"/></svg>Water leakage<br>through cracks</div>
  <svg class="signs-line" width="803" height="1039" style="pointer-events:none">
    <polyline points="41,932 238,932 249,921 748,921 762,899" fill="none" stroke="var(--green)" stroke-width=".8"/>
    <circle cx="41" cy="932" r="2" fill="var(--green-light)"/><circle cx="762" cy="899" r="2" fill="var(--green-light)"/>
  </svg>

  <p class="closing" style="left:41px">If you suspect issues with your post-tension cables or need a routine inspection, don't hesitate to contact us. Our experts are ready to provide the best solutions to keep your structures safe and secure.</p>
  <p class="closing" style="left:415px;width:360px">Ensure the safety and longevity of your building with our professional post-tension cable repair services. Trust us to deliver quality and reliability every time.</p>

  <svg class="footer-bar" width="803" height="12">
    <polygon points="0,0 405,0 400,12 0,12" fill="var(--green)"/>
    <polygon points="414,0 803,0 803,12 409,12" fill="var(--grey-chev)"/>
  </svg>
</main>
</body>
</html>
```